Polling Insight Bureau Wordpress Web Design

Polling Insight Bureau, in association with The Halvern Institute at The University of Eastbrook Vale, needs a 5-page Wordpress website designed from scratch. Using the provided logos/font/color palette
We need a nicely designed site (based on the color scheme, font, and logo that we provided) that is 5 pages.
What I am thinking is:
1)Home Page - a brief breakdown of what the Polling Insight Bureau is, how it relates to the University and The Halvern Institute
2)About - 3-4 biography sections about the employees of the PIB with headshots
3)Our Work - A page about the clients they have worked with in the past, testimonials/case studies, and maybe a scroll of logos from clients they have worked with
4)Capabilities - a breakdown of 3-4 segmented sections describing the work that they do and their ideal target markets
5)Contact Us - a contact form that we can redirect to the manager

Please use College/University and Maine stock photos as place holders. Lorem Ipsum and stock images are completely fine.
Please note that we are in the process of collecting the final text copy for the website. Designers can use text place holders for the time being. The winner will then be ask to use the final content.

University faculty, Local and regional non-profits and government agencies

Data analysis, Surveying, B2B, Higher Education

Coded - Design and coding required

5+ page

Serif
Sans Serif

Must have
• footer must mention "a division of The Halvern Institute" (logo attached).

```html
<!DOCTYPE html>
<html lang="en">
<head>
<meta charset="utf-8">
<title>Polling Insight Bureau – Home</title>
<link href="https://fonts.googleapis.com/css2?family=Montserrat:wght@400;500;600;700;800&display=swap" rel="stylesheet">
<style>
:root{
  --orange:#f26b4a;
  --coral:#e8505b;
  --plum:#5e1747;
  --magenta:#a32b7c;
  --ink:#2a1b26;
  --text:#4a4250;
  --muted:#8a8290;
  --line:#e3dde3;
  --paper:#ffffff;
  --mist:#f6f3f6;
}
*{box-sizing:border-box;margin:0;padding:0}
html,body{width:1200px;height:3136px;overflow:hidden}
body{font-family:"Montserrat",sans-serif;color:var(--text);background:var(--paper);position:relative}
.section{position:absolute;left:0;width:1200px}
.wordmark{display:flex;align-items:center;gap:10px;font-weight:700;color:var(--orange);font-size:22px;letter-spacing:.5px}
.wordmark .dot{width:16px;height:16px;border-radius:50%;background:var(--orange)}
.btn{display:inline-block;border-radius:30px;font-weight:600;font-size:13px;padding:11px 26px;color:#fff;background:var(--orange)}

/* brand strip */
.brand{top:0;height:240px;background:var(--mist);display:flex;align-items:center;justify-content:center;gap:120px}
.brand .wordmark{font-size:30px}
.brand .spec h4{font-size:14px;font-weight:600;color:var(--ink);margin-bottom:10px}
.brand .spec p{font-size:14px;color:var(--muted)}
.swatches{display:flex;gap:8px}
.swatches span{width:34px;height:34px;border-radius:6px}

/* nav */
.nav{top:240px;height:90px;display:flex;align-items:center;justify-content:space-between;padding:0 70px;border-bottom:1px solid var(--line)}
.nav ul{display:flex;gap:10px;list-style:none;align-items:center}
.nav li{font-size:13px;font-weight:600;color:var(--ink);padding:10px 18px;border-radius:24px}
.nav li.active{background:var(--orange);color:#fff}
.nav li.quote{background:var(--plum);color:#fff;margin-left:14px}

/* hero */
.hero{top:330px;height:600px;overflow:hidden}
.hero-photo{position:absolute;inset:0;background:linear-gradient(120deg,#3a2630 0%,#6b4a48 45%,#2d1f25 100%)}
.hero-shade{position:absolute;inset:0;background:linear-gradient(180deg,rgba(20,10,18,.35),rgba(20,10,18,.55))}
.hero-copy{position:absolute;top:190px;width:100%;text-align:center;color:#fff}
.hero-copy h1{font-size:54px;font-weight:700;margin-bottom:10px}
.hero-copy p{font-size:24px;font-weight:400;line-height:1.35;margin-bottom:30px}
.hero svg{position:absolute;bottom:0;left:0}

/* about */
.about{top:930px;height:510px;display:flex;align-items:center;padding:0 90px;gap:70px}
.about-copy{width:480px}
.about-copy h2{font-size:32px;color:var(--orange);font-weight:700;margin-bottom:22px}
.about-copy h3{font-size:16px;color:var(--ink);font-weight:700;line-height:1.45;margin-bottom:16px}
.about-copy p{font-size:13px;line-height:1.7;margin-bottom:14px}
.about-copy .btn{margin-top:14px}
.about-frame{width:470px;height:360px;border-radius:34px;padding:10px;background:linear-gradient(135deg,var(--magenta),var(--orange))}
.about-photo{width:100%;height:100%;border-radius:26px;background:linear-gradient(135deg,#cfc6c2,#9a8f8c 60%,#7d716f)}

/* relationship */
.relation{top:1440px;height:520px;overflow:hidden}
.relation-bg{position:absolute;inset:0;background:linear-gradient(90deg,var(--plum),var(--magenta) 55%,#c23a7e)}
.relation svg{position:absolute;left:0}
.relation-inner{position:absolute;top:130px;left:110px;right:90px;display:flex;gap:70px;align-items:center}
.partner-card{width:300px;height:230px;background:#fff;border-radius:24px;border:6px solid var(--orange);display:flex;flex-direction:column;align-items:center;justify-content:center;gap:12px}
.partner-card .name{font-size:24px;font-weight:700;color:var(--plum)}
.partner-card .sub{font-size:10px;color:var(--muted)}
.relation-copy{color:#fff;width:560px}
.relation-copy h2{font-size:30px;font-weight:700;margin-bottom:16px}
.relation-copy h3{font-size:16px;font-weight:600;line-height:1.45;margin-bottom:14px}
.relation-copy p{font-size:13px;line-height:1.7;margin-bottom:22px;opacity:.9}

/* stats */
.stats{top:1960px;height:360px;display:flex;align-items:center;padding:0 90px;gap:80px}
.stat{position:relative;width:400px;height:240px}
.stat-map{position:absolute;inset:0;border-radius:20px;background:radial-gradient(ellipse at center,#e9e4ea,#fff 70%)}
.stat-num{position:absolute;top:60px;left:120px}
.stat-num strong{display:block;font-size:90px;font-weight:800;color:var(--orange);line-height:1}
.stat-num span{font-size:13px;color:var(--muted);font-weight:600}
.clients{display:grid;grid-template-columns:repeat(4,110px);gap:30px 36px}
.clients span{height:56px;border-radius:10px;background:var(--mist);border:1px solid var(--line)}

/* inquiry */
.inquiry{top:2320px;height:460px;display:flex;justify-content:center;align-items:center}
.inquiry-card{width:620px;height:400px;border:4px solid var(--orange);border-radius:30px;padding:34px 80px;background:#fff}
.inquiry-card h2{text-align:center;color:var(--orange);font-size:30px;font-weight:600;margin-bottom:26px}
.row{display:flex;gap:18px;margin-bottom:16px}
.field{flex:1;height:40px;border:1px solid var(--line);border-radius:6px;font-size:12px;color:var(--muted);padding:12px 14px}
.field.tall{height:80px}
.inquiry-card .btn{display:block;width:140px;margin:6px auto 0;text-align:center}

/* footer */
.footer{top:2780px;height:356px;overflow:hidden;color:#fff}
.footer-photo{position:absolute;inset:0;background:linear-gradient(120deg,#2d1b25,#4a2e35 50%,#22151c)}
.footer-inner{position:absolute;top:50px;left:90px;right:90px;display:flex;justify-content:space-between}
.footer .wordmark{margin-top:60px}
.footer h4{color:var(--orange);font-size:16px;font-weight:700;margin-bottom:16px}
.contact li{display:flex;gap:10px;font-size:12px;line-height:1.5;margin-bottom:12px;list-style:none}
.contact svg{flex:none;margin-top:2px}
.links li{list-style:none;font-size:12px;margin-bottom:9px}
.division{width:220px;height:170px;background:#fff;border-radius:20px;border:5px solid var(--orange);display:flex;flex-direction:column;align-items:center;justify-content:center;gap:8px;color:var(--plum)}
.division .name{font-size:20px;font-weight:700}
.division .sub{font-size:10px;color:var(--muted)}
.footer-bar{position:absolute;bottom:0;left:0;right:0;height:46px;border-top:1px solid rgba(255,255,255,.2);display:flex;align-items:center;justify-content:space-between;padding:0 90px;font-size:11px}
.socials{display:flex;gap:10px}
.socials span{width:20px;height:20px;border-radius:50%;border:1px solid rgba(255,255,255,.6)}
</style>
</head>
<body>

<section class="section brand">
  <div class="wordmark"><span class="dot"></span>Polling Insight Bureau</div>
  <div class="spec"><h4>Fonts:</h4><p>Montserrat</p></div>
  <div class="spec"><h4>Colors:</h4>
    <div class="swatches"><span style="background:var(--plum)"></span><span style="background:var(--magenta)"></span><span style="background:var(--coral)"></span><span style="background:var(--orange)"></span></div>
  </div>
</section>

<header class="section nav">
  <div class="wordmark"><span class="dot"></span>Polling Insight Bureau</div>
  <ul>
    <li class="active">Home</li><li>About Us</li><li>Our Work</li><li>Capabilities</li><li>Contact Us</li><li class="quote">Get a Quote</li>
  </ul>
</header>

<section class="section hero">
  <div class="hero-photo" role="img" aria-label="Photo of hands typing on a laptop at a desk"></div>
  <div class="hero-shade"></div>
  <div class="hero-copy">
    <h1>Lorem Ipsum</h1>
    <p>is simply dummy text of the printing and<br>typesetting industry.</p>
    <span class="btn">Explore More</span>
  </div>
  <svg width="1200" height="80" viewBox="0 0 1200 80"><path d="M0 40 Q600 110 1200 40 L1200 80 L0 80Z" fill="var(--orange)"/><path d="M0 52 Q600 122 1200 52 L1200 80 L0 80Z" fill="#fff"/></svg>
</section>

<section class="section about">
  <div class="about-copy">
    <h2>Polling Insight Bureau</h2>
    <h3>Lorem Ipsum is simply dummy text of the printing and typesetting industry.</h3>
    <p>Lorem Ipsum has been the industry's standard dummy text ever since the 1500s, when an unknown printer took a galley of type and scrambled it to make a type specimen book.</p>
    <p>It has survived not only five centuries, but also the leap into electronic typesetting, remaining essentially unchanged.</p>
    <span class="btn">Explore More</span>
  </div>
  <div class="about-frame"><div class="about-photo" role="img" aria-label="Photo of a person with a laptop beside a survey checklist"></div></div>
</section>

<section class="section relation">
  <div class="relation-bg"></div>
  <svg width="1200" height="70" viewBox="0 0 1200 70" style="top:0"><path d="M0 0 H1200 V20 Q600 90 0 20Z" fill="#fff"/></svg>
  <svg width="1200" height="70" viewBox="0 0 1200 70" style="bottom:0"><path d="M0 50 Q600 -20 1200 50 V70 H0Z" fill="var(--orange)"/><path d="M0 62 Q600 -8 1200 62 V70 H0Z" fill="#fff"/></svg>
  <div class="relation-inner">
    <div class="partner-card"><span class="name">Halvern Institute</span><span class="sub">a research partner</span></div>
    <div class="relation-copy">
      <h2>Relationship with the Halvern Institute</h2>
      <h3>Lorem Ipsum is simply dummy text of the printing and typesetting industry.</h3>
      <p>Lorem Ipsum has been the industry's standard dummy text ever since the 1500s, when an unknown printer took a galley of type and scrambled it to make a type specimen book.</p>
      <span class="btn">Explore More</span>
    </div>
  </div>
</section>

<section class="section stats">
  <div class="stat">
    <div class="stat-map" role="img" aria-label="Faint world map"></div>
    <div class="stat-num"><strong>15+</strong><span>Years in World Wide</span></div>
  </div>
  <div class="clients" aria-label="Client badges">
    <span></span><span></span><span></span><span></span><span></span><span></span><span></span><span></span>
  </div>
</section>

<section class="section inquiry">
  <div class="inquiry-card">
    <h2>Quick Inquiry</h2>
    <div class="row"><div class="field">Name</div><div class="field">Phone</div></div>
    <div class="row"><div class="field">Email</div></div>
    <div class="row"><div class="field tall">Message</div></div>
    <span class="btn">Submit</span>
  </div>
</section>

<footer class="section footer">
  <div class="footer-photo" role="img" aria-label="Dark photo of a workspace with laptop"></div>
  <div class="footer-inner">
    <div class="wordmark"><span class="dot"></span>Polling Insight Bureau</div>
    <div class="contact">
      <h4>Contact Info</h4>
      <ul>
        <li><svg width="14" height="16" viewBox="0 0 14 16"><path d="M7 0C3 0 0 3 0 6.5 0 11 7 16 7 16s7-5 7-9.5C14 3 11 0 7 0Zm0 9a2.5 2.5 0 1 1 0-5 2.5 2.5 0 0 1 0 5Z" fill="var(--orange)"/></svg><span>Address<br>14 Vale Commons, Eastbrook<br>Suite 200, ZIP 00000</span></li>
        <li><svg width="14" height="14" viewBox="0 0 14 14"><path d="M3 0l2 3-1.5 1.5a8 8 0 0 0 6 6L11 9l3 2-1.5 3C6 14 0 8 0 1.5Z" fill="var(--orange)"/></svg><span>(555) 014-2290</span></li>
        <li><svg width="14" height="12" viewBox="0 0 14 12"><rect width="14" height="12" rx="2" fill="var(--orange)"/><path d="M1 2l6 5 6-5" stroke="#fff" fill="none"/></svg><span>hello@pollinginsight.example</span></li>
      </ul>
    </div>
    <div class="links">
      <h4>Quick Links</h4>
      <ul><li>Home</li><li>About Us</li><li>Our Work</li><li>Capabilities</li><li>Contact Us</li></ul>
    </div>
    <div class="division"><span class="sub">a division of</span><span class="name">Halvern Institute</span><span class="sub">The University of Eastbrook Vale</span></div>
  </div>
  <div class="footer-bar">
    <span>Copyright © 2020 Polling Insight Bureau. All Rights Reserved.</span>
    <div class="socials"><span></span><span></span><span></span><span></span></div>
  </div>
</footer>

</body>
</html>
```